deceased estate clean ups brochures

we would like a brochure to reresent our business we already have new web site and want to do DL A4 brochure to give out to promote our business we already have logo www.larkmore.com.au is where you can get all info needed

Target Market(s)

families with loved ones that have past away
people done sizing or needing to decluter

Colors
cadf82
33b8a4
886aae
33a6d7

```html
<!DOCTYPE html>
<html lang="en">
<head>
<meta charset="utf-8">
<title>Larkmore – Services Offered</title>
<link rel="stylesheet" href="https://fonts.googleapis.com/css2?family=Nunito+Sans:wght@800;900&family=Source+Sans+3:wght@300;400&display=swap">
<style>
:root{
  --lime:#cadf82;
  --teal:#33b8a4;
  --purple:#886aae;
  --ink:#111111;
  --text:#2a2a2a;
  --paper:#ffffff;
}
*{box-sizing:border-box;margin:0;padding:0}
html,body{width:1200px;height:848px;overflow:hidden;background:var(--paper)}
.spread{position:relative;width:1200px;height:848px;font-family:"Source Sans 3",sans-serif;font-weight:300;color:var(--text);font-size:10.2px;line-height:12px}
.band{position:absolute;height:19px;width:405px}
.band--top{top:0}
.band--bottom{bottom:0;height:18px}
.band--lime{left:0;background:var(--lime)}
.band--teal{left:405px;background:var(--teal)}
.band--purple{left:810px;width:390px;background:var(--purple)}
.hero{position:absolute;top:19px;height:141px}
.hero--supplies{left:0;width:405px;background:linear-gradient(100deg,#f1d7a8 0%,#e7a9c4 22%,#b5d7ef 45%,#3f8fd6 62%,#63c25b 80%,#bfe3f2 100%)}
.hero--movers{left:406px;width:404px;background:linear-gradient(100deg,#c9dcec 0%,#9fb9d6 30%,#3a4f8a 50%,#c69c6b 70%,#d8b98c 85%,#bcc7d4 100%)}
.hero--couple{left:811px;width:389px;background:linear-gradient(100deg,#9a4a35 0%,#b7634b 35%,#d9cfc2 55%,#7b6a99 70%,#c4b6a6 85%,#4f7b3a 100%)}
.fold{position:absolute;top:19px;height:811px;border-left:1.5px dashed var(--ink)}
.fold--one{left:405px}
.fold--two{left:810px}
.page-title{position:absolute;left:25px;top:180px;font-family:"Nunito Sans",sans-serif;font-weight:900;font-size:33px;line-height:36px;color:var(--ink);letter-spacing:.3px}
.section-title{position:absolute;left:25px;top:392px;font-family:"Nunito Sans",sans-serif;font-weight:900;font-size:21px;line-height:24px;color:var(--ink)}
.service{position:absolute;display:grid;grid-template-columns:115px 1fr;column-gap:7px}
.service--c1{left:25px;width:362px}
.service--c2{left:427px;width:362px}
.service--c3{left:825px;width:362px}
.service__photo{width:115px;height:101px}
.service__title{font-family:"Nunito Sans",sans-serif;font-weight:900;font-size:13.4px;line-height:15.5px;color:var(--ink);margin-bottom:9px}
.service__body p{margin-bottom:12px}
.service__body p:last-child{margin-bottom:0}
.checklist{list-style:none;margin:0 0 0 22px}
.checklist li{position:relative;padding-left:10px}
.checklist li::before{content:"";position:absolute;left:1px;top:3px;width:3px;height:6px;border:solid var(--ink);border-width:0 1.5px 1.5px 0;transform:rotate(40deg)}
.photo--carer{background:linear-gradient(120deg,#f4e6dc,#d9b8a3 55%,#8a8f98)}
.photo--cluttered-room{background:linear-gradient(120deg,#c9c3bd,#7a5c4a 50%,#3b3340)}
.photo--bare-room{background:linear-gradient(120deg,#d8d2c8,#a59c8f 55%,#6f6a63)}
.photo--house-build{background:linear-gradient(160deg,#8fb7dc,#e6e4df 45%,#b78a5d)}
.photo--cleaners{background:linear-gradient(120deg,#eeeae4,#d7c9b8 50%,#2e3c5a)}
.photo--ladders{background:linear-gradient(160deg,#d8dbe0,#a9a39d 50%,#7b4a3a)}
.photo--couple-chair{background:linear-gradient(120deg,#ebe7e1,#c9c1b6 50%,#6f6c6c)}
.photo--garden{background:linear-gradient(130deg,#5d9a3a,#87c35a 50%,#6b5538)}
</style>
</head>
<body>
<main class="spread">
  <div class="band band--top band--lime"></div>
  <div class="band band--top band--teal"></div>
  <div class="band band--top band--purple"></div>

  <div class="hero hero--supplies" role="img" aria-label="Basket of cleaning supplies in front of blossoms"></div>
  <div class="hero hero--movers" role="img" aria-label="Two removalists carrying cardboard boxes from a van"></div>
  <div class="hero hero--couple" role="img" aria-label="Senior couple sitting on a garden bench outside a brick home"></div>

  <div class="fold fold--one"></div>
  <div class="fold fold--two"></div>

  <h1 class="page-title">SERVICES OFFERED</h1>

  <section class="service service--c1" style="top:236px">
    <div class="service__photo photo--carer" role="img" aria-label="Carer assisting an elderly woman"></div>
    <div class="service__body">
      <h2 class="service__title">SENIOR / AGED CARE RELOCATIONS AND DOWN SIZING</h2>
      <p>If you’re relocating into age care or downsizing your living arrangements, Larkmore offers you a complete service to assist you in moving to your new home. More Australian seniors are opting to sell their homes and buy a property in a retirement complex. It can be a daunting experience as there are so many things to organise and prepare.</p>
    </div>
  </section>

  <h2 class="section-title">DECEASED ESTATES</h2>

  <section class="service service--c1" style="top:425px">
    <div class="service__photo photo--cluttered-room" role="img" aria-label="Cluttered room full of belongings"></div>
    <div class="service__body">
      <h2 class="service__title">HOUSE CLEARING</h2>
      <p>We can work with family or trustees in providing services to prepare the property for rental or sale.</p>
      <p>Following the loss of a family member, many people will find the thought of dealing with the clearance of personal effects and property in a deceased estate a daunting one.</p>
      <p>We understand the difficulties with making arrangements at this time and offer a tailored service to assist with your personal situation.</p>
    </div>
  </section>

  <section class="service service--c1" style="top:625px">
    <div class="service__photo photo--bare-room" role="img" aria-label="Empty room under renovation"></div>
    <div class="service__body">
      <h2 class="service__title">PREPARATION FOR SALE</h2>
      <p>Tidying up before selling your house? In need of an estate clean up? Doing renovations or construction, or are in need of an alternative to skips we can help.</p>
      <p>We take almost anything that is non-hazardous that two people can lift: old unwanted furniture and appliances, garden waste, house and renovation debris, excess packaging and cardboard, office furniture and equipment, electronics and TVs – we take it all, whether you have a lot or a little.</p>
      <p>We make sure it gets disposed of properly through donation or recycling. The dump is always our last resort.</p>
    </div>
  </section>

  <section class="service service--c2" style="top:236px">
    <div class="service__photo photo--house-build" role="img" aria-label="House under construction with ladders and paint tins"></div>
    <div class="service__body">
      <h2 class="service__title">COSMETIC REPAIRS AND HOUSE MAINTENANCE</h2>
      <p>At Larkmore, we are experienced in cosmetic house repairs and renovations.</p>
      <p style="margin-bottom:0">Common additional services requested by our customers include:</p>
      <ul class="checklist">
        <li>Plastering</li>
        <li>Painting</li>
        <li>New carpets or floorboards</li>
        <li>Electrical &amp; Plumbing (by Licensed Tradespeople)</li>
        <li>Bathroom and kitchen renovations</li>
        <li>Garden maintenance and landscaping</li>
        <li>Fencing</li>
        <li>Brickwork</li>
        <li>Decking</li>
      </ul>
      <p>We make sure it gets disposed of properly through donation or recycling. The dump is always our last resort.</p>
    </div>
  </section>

  <section class="service service--c2" style="top:502px">
    <div class="service__photo photo--cleaners" role="img" aria-label="Cleaning team wiping and mopping an apartment"></div>
    <div class="service__body">
      <h2 class="service__title">CLEANING SERVICE</h2>
      <p>We can provide a Cleaning Service for a house sale or rental preparation or a deceased estate. Houses need to be cleared for the property market, but they also need to be cleaned thoroughly. Let us make these decisions easier for you, hassle free and within your budget.</p>
      <p>By using our professional team to prepare your property, you are guaranteed that our experience will make your life a lot easier, especially dealing with those hard decisions.</p>
      <p>We take almost anything that is non-hazardous that two people can lift: old unwanted furniture and appliances, garden waste, house and renovation debris, excess packaging and cardboard, office furniture and equipment, electronics and TVs – we take it all, whether you have a lot or a little.</p>
      <p>We make sure it gets disposed of properly through donation or recycling. The dump is always our last resort.</p>
    </div>
  </section>

  <section class="service service--c3" style="top:236px">
    <div class="service__photo photo--ladders" role="img" aria-label="Tradesmen on ladders repairing a house facade"></div>
    <div class="service__body">
      <h2 class="service__title">COSMETIC REPAIRS AND HOUSE MAINTENANCE</h2>
      <p>At Larkmore, we are experienced in Cosmetic Repairs, House Maintenance and house renovations and we can help you achieve the maximum return on the renting or sale of your property.</p>
    </div>
  </section>

  <section class="service service--c3" style="top:375px">
    <div class="service__photo photo--couple-chair" role="img" aria-label="Couple moving an armchair into a new home"></div>
    <div class="service__body">
      <h2 class="service__title">PREPARATION FOR RENTAL OR SALE</h2>
      <p>Our target is to create maximum appeal on all aspects of your property, allowing you to sell or rent and attract a higher sale price when properly prepared and presented.</p>
      <p>We can advise you whether you need to make any cosmetic updates or repairs to improve your home’s resale value.</p>
      <p>We can do cosmetic renovations, clean and declutter your entire home from top to bottom. We will leave you with a clean, tidy and market ready house ready to sell, rent or move into.</p>
    </div>
  </section>

  <section class="service service--c3" style="top:578px">
    <div class="service__photo photo--garden" role="img" aria-label="Gloved hand planting in a garden bed"></div>
    <div class="service__body">
      <h2 class="service__title">GARDEN MAKEOVERS</h2>
      <p>We run a successful landscaping business, The Fernvale Group Signature Division, offering a full service in landscaping and construction.</p>
      <p>With more than 20 years’ experience in the landscape and construction industry, we can offer solid, well-founded advice, excellent material selection and landscapes that grow into amazing spaces. Whether you choose to landscape for resale or to enjoy your new outdoor space.</p>
      <p>We, at The Fernvale Group, pride ourselves on high-quality professional service from the start to the completion of each and every job, including:</p>
      <p>Ongoing garden maintenance by qualified staff to keep your job looking as good as when it was completed.</p>
    </div>
  </section>

  <div class="band band--bottom band--lime"></div>
  <div class="band band--bottom band--teal"></div>
  <div class="band band--bottom band--purple"></div>
</main>
</body>
</html>
```